Business Card Design Project

Need a business card that stands my education platform as a whole but

Target Market(s)

Parents, families, expats in the middle east.

Industry/Entity Type

Education

Contact Information for Business Card

www.brightlane.ae
www.homesteadhub.ae
www.littlenestcarers.ae

+971552419736
helena@brightlane.ae

Font styles to use
Serif

Requirements
Must have
• Logo's and contact details

```html
<!DOCTYPE html>
<html lang="en">
<head>
<meta charset="utf-8">
<title>Brightlane Business Card</title>
<link href="https://fonts.googleapis.com/css2?family=Tinos:wght@400;700&display=swap" rel="stylesheet">
<style>
  :root {
    --teal: #438ea8;
    --teal-deep: #3a87a3;
    --orange: #f0903a;
    --card: #ffffff;
    --faint: #e6e6e6;
    --photo-a: #d9cfc6;
    --photo-b: #8a5a3c;
  }
  * { margin: 0; padding: 0; box-sizing: border-box; }
  html, body {
    width: 1200px;
    height: 997px;
    overflow: hidden;
  }
  body {
    background: var(--teal);
    font-family: "Tinos", "Times New Roman", serif;
    position: relative;
  }
  .card {
    position: absolute;
    width: 540px;
    height: 318px;
    background: var(--card);
  }
  .card--front { left: 31px; top: 340px; }
  .card--back { left: 617px; top: 340px; }

  /* Front */
  .front-tagline {
    position: absolute;
    left: 0; right: 0;
    text-align: center;
    color: var(--orange);
    font-size: 15px;
    line-height: 20px;
    letter-spacing: 1.2px;
  }
  .front-tagline--top { top: 18px; }
  .front-tagline--bottom { top: 265px; }
  .brand-lockup {
    position: absolute;
    left: 0; right: 0;
    top: 108px;
    display: flex;
    flex-direction: column;
    align-items: center;
    gap: 14px;
  }
  .brand-name {
    display: flex;
    align-items: center;
    gap: 12px;
    color: var(--teal);
    font-size: 40px;
    letter-spacing: 3px;
    line-height: 1;
  }
  .brand-dot {
    width: 16px; height: 16px;
    border-radius: 50%;
    background: var(--orange);
  }
  .brand-descriptor {
    color: var(--teal);
    font-size: 14px;
    letter-spacing: 1.5px;
  }

  /* Back */
  .holder-name {
    position: absolute;
    left: 33px; top: 36px;
    color: var(--teal-deep);
    font-size: 20px;
    font-weight: 700;
    letter-spacing: 2.2px;
  }
  .brand-watermark {
    position: absolute;
    left: 300px; top: 110px;
    width: 220px;
    text-align: center;
    color: var(--faint);
    font-size: 34px;
    letter-spacing: 3px;
  }
  .portrait {
    position: absolute;
    left: 33px; top: 110px;
    width: 173px; height: 176px;
    border-radius: 86px 86px 0 0;
    background: linear-gradient(160deg, var(--photo-a) 0%, var(--photo-b) 100%);
  }
  .contact {
    position: absolute;
    left: 227px;
    font-size: 17px;
    line-height: 28px;
    letter-spacing: 1.3px;
    list-style: none;
  }
  .contact--direct { top: 128px; color: var(--orange); }
  .contact--web { top: 211px; color: var(--teal-deep); }
</style>
</head>
<body>
  <section class="card card--front">
    <p class="front-tagline front-tagline--top">Raise children with an enquiring mind<br>who love to learn</p>
    <div class="brand-lockup">
      <div class="brand-name"><span class="brand-dot"></span>Brightlane</div>
      <div class="brand-descriptor">Accelerated Learning Centre</div>
    </div>
    <p class="front-tagline front-tagline--bottom">Unique opportunity to join your child on their<br>learning journey</p>
  </section>

  <section class="card card--back">
    <div class="brand-watermark">Brightlane</div>
    <h1 class="holder-name">HELENA VAROS</h1>
    <div class="portrait" role="img" aria-label="Portrait photograph of Helena Varos"></div>
    <ul class="contact contact--direct">
      <li>+971 552419736</li>
      <li>helena@brightlane.ae</li>
    </ul>
    <ul class="contact contact--web">
      <li>www.brightlane.ae</li>
      <li>www.homesteadhub.ae</li>
      <li>www.littlenestcarers.ae</li>
    </ul>
  </section>
</body>
</html>
```